Tildens Biscuit Barn Website

I need a website for a diner/restaurant that has been established in a farming, oil and industrial community for over 15 years. The website needs to be simple in design, but that should demonstrate the mastery of skills of the designer. Our diner/restaurant is family oriented, patriotic but very rustic
Fb Address is fb.me/TildensBarn

Pictures of the restaurant

https://www.filecrate-example.net/s/qk72hdw01/Tildens_05.jpg

Pictures of About us

https://www.filecrate-example.net/sh/zm40vrt88/AboutUsPhotos

Article about Tilden's
https://www.filecrate-example.net/s/wp31nbx57/TildensBiscuitBarn1.PDF
https://www.filecrate-example.net/s/hy65lcu29/TildensBiscuitBarn2.PDF

Reason: I was slow to update with information.

Reason: I am just getting feedback to the designs posted. I wasn't sure of the limited feedback was limiting designers from submitting designs. That and running a business with 25 employees open 12 hours a day, being here 2 hours prior and 2-3 hours after makes for long days.

I've increased the first place prize and also added funds to the second and third place prizes for your effort.

I just need the files in PSD, not HTML 5 as originally requested. We can handle getting the coding part.

Ill have the contest finalized by Monday. Thanks for your patience.

Target Market(s)

Cross section of adults from 18-35 & 35-55.

Industry/Entity Type

Industrial

Font styles to use
Other font styles liked:
• ff tisa web pro or garamond premier pro

Requirements
Must have
• Must be clean, look nice and not look like an afterthought.
Nice to have
• Please see the last two documents for information about our restaurant, which was featured in our local newspaper.

```html
<!DOCTYPE html>
<html lang="en">
<head>
<meta charset="utf-8">
<title>Tilden's Biscuit Barn</title>
<link rel="stylesheet" href="https://fonts.googleapis.com/css2?family=Ubuntu:wght@500;700&family=Roboto:ital,wght@1,400&family=Lato:wght@400;700&display=swap">
<style>
  :root {
    --brand-red: #d10a0a;
    --leaf-green: #8cc63f;
    --leaf-green-dark: #5d8f23;
    --sky: #5ab4da;
    --caption: rgba(110, 195, 230, 0.82);
    --ink: #333333;
    --nav-ink: #555555;
    --night: #131718;
    --cream: #ebe7d7;
    --white: #ffffff;
  }
  * { margin: 0; padding: 0; box-sizing: border-box; }
  html, body { width: 1200px; height: 844px; overflow: hidden; background: var(--white); }
  .page { position: relative; width: 1200px; height: 844px; overflow: hidden; font-family: "Lato", sans-serif; }

  .hero-photo {
    position: absolute; left: 0; top: 0; width: 1200px; height: 688px;
    background:
      radial-gradient(ellipse 120px 160px at 1150px 470px, rgba(90, 170, 90, 0.85), rgba(90, 170, 90, 0) 100%),
      radial-gradient(ellipse 70px 60px at 960px 150px, rgba(70, 150, 80, 0.55), rgba(70, 150, 80, 0) 100%),
      radial-gradient(ellipse 240px 140px at 470px 380px, rgba(250, 200, 120, 0.9), rgba(250, 200, 120, 0) 100%),
      radial-gradient(ellipse 220px 130px at 810px 300px, rgba(252, 215, 120, 0.85), rgba(252, 215, 120, 0) 100%),
      radial-gradient(ellipse 260px 110px at 330px 180px, rgba(240, 160, 80, 0.8), rgba(240, 160, 80, 0) 100%),
      radial-gradient(ellipse 300px 120px at 300px 560px, rgba(240, 140, 90, 0.85), rgba(240, 140, 90, 0) 100%),
      radial-gradient(ellipse 200px 160px at 1100px 340px, rgba(245, 175, 80, 0.75), rgba(245, 175, 80, 0) 100%),
      linear-gradient(160deg, rgba(40, 28, 24, 0) 30%, rgba(40, 28, 24, 0.55) 38%, rgba(40, 28, 24, 0) 46%),
      linear-gradient(200deg, rgba(35, 25, 22, 0) 50%, rgba(35, 25, 22, 0.5) 58%, rgba(35, 25, 22, 0) 66%),
      linear-gradient(180deg, #6e4a36 0%, #c97a3a 30%, #d98a3f 55%, #a65a30 80%, #4a3026 100%);
  }
  .night-band { position: absolute; left: 0; top: 688px; width: 1200px; height: 66px; background: var(--night); }
  .footer-shape { position: absolute; left: 0; top: 754px; }

  .header-shape { position: absolute; left: 0; top: 0; }
  .top-line { position: absolute; left: 0; top: 0; width: 1200px; height: 3px; background: var(--leaf-green); }
  .brand {
    position: absolute; left: 141px; top: 24px; font-family: "Ubuntu", sans-serif; font-weight: 700;
    font-size: 27px; line-height: 1.05; color: var(--brand-red); letter-spacing: 0.5px;
  }
  .contact { position: absolute; top: 12px; font-family: "Ubuntu", sans-serif; font-size: 14px; color: var(--ink); display: flex; align-items: center; gap: 5px; }
  .contact.phone { left: 637px; font-weight: 700; }
  .contact.email { left: 769px; font-weight: 500; }
  .book-button {
    position: absolute; left: 934px; top: 3px; width: 133px; height: 33px; background: var(--leaf-green);
    color: var(--white); font-family: "Ubuntu", sans-serif; font-weight: 500; font-size: 15px;
    display: flex; align-items: center; justify-content: center; border-radius: 0 0 3px 3px;
  }
  .header-rule { position: absolute; left: 440px; top: 47px; width: 680px; height: 1px; background: #e4e4e4; }
  .main-nav { position: absolute; top: 52px; left: 447px; height: 44px; display: flex; font-family: "Ubuntu", sans-serif; font-weight: 500; font-size: 16px; }
  .main-nav a { color: var(--nav-ink); text-decoration: none; display: flex; align-items: center; justify-content: center; position: relative; }
  .main-nav a + a::before { content: ""; position: absolute; left: 0; top: 11px; width: 1px; height: 22px; background: #dddddd; }
  .main-nav a.active { background: var(--brand-red); color: var(--white); border-radius: 3px 3px 0 0; }

  .caption-bar { position: absolute; left: 131px; top: 556px; width: 938px; height: 66px; background: var(--caption); }
  .caption-text { position: absolute; left: 20px; top: 15px; font-family: "Roboto", sans-serif; font-style: italic; font-size: 28px; color: #111; letter-spacing: 0.6px; }
  .slider-dots { position: absolute; right: 14px; top: 26px; display: flex; gap: 5px; }
  .slider-dots span { width: 15px; height: 15px; border-radius: 50%; background: #1f6e8f; }
  .slider-dots span.current { background: #5aa3c2; }

  .feature-panel { position: absolute; left: 131px; top: 622px; width: 938px; height: 166px; background: var(--white); }
  .welcome-shape { position: absolute; left: 0; top: 0; }
  .welcome-eyebrow { position: absolute; left: 21px; top: 24px; font-family: Arial, Helvetica, sans-serif; font-size: 22px; color: var(--ink); }
  .welcome-title { position: absolute; left: 21px; top: 51px; font-family: Arial, Helvetica, sans-serif; font-weight: 700; font-size: 25px; color: var(--ink); }
  .welcome-body { position: absolute; left: 22px; top: 80px; width: 300px; font-size: 14.5px; line-height: 23px; color: var(--ink); }
  .feature { position: absolute; top: 27px; width: 180px; text-align: center; }
  .feature svg { display: block; margin: 0 auto; }
  .feature-label { margin-top: 12px; font-family: Arial, Helvetica, sans-serif; font-weight: 700; font-size: 15.5px; letter-spacing: 1px; color: var(--ink); }
  .feature-divider { position: absolute; top: 11px; width: 1px; height: 144px; background: linear-gradient(#fff, #d8d8d8, #fff); }

  .copyright { position: absolute; left: 136px; top: 809px; font-size: 14px; color: var(--white); }
  .newsletter-icon { position: absolute; left: 544px; top: 800px; }
  .newsletter-input {
    position: absolute; left: 585px; top: 801px; width: 197px; height: 31px; background: var(--white);
    border: 1px solid #cfe4ee; font-family: "Lato", sans-serif; font-size: 14px; color: #777; padding-left: 7px;
    display: flex; align-items: center;
  }
  .newsletter-go {
    position: absolute; left: 782px; top: 801px; width: 39px; height: 31px;
    background: linear-gradient(var(--leaf-green), var(--leaf-green-dark)); color: var(--white);
    font-family: "Ubuntu", sans-serif; font-weight: 700; font-size: 15px; display: flex; align-items: center; justify-content: center;
  }
  .social-links { position: absolute; left: 940px; top: 805px; display: flex; gap: 7px; }
  .social-links span { width: 24px; height: 24px; border-radius: 50%; background: #2b7ea3; }
</style>
</head>
<body>
<div class="page">
  <div class="hero-photo" role="img" aria-label="Close-up photo of golden glazed pastries and croissants on dark serving trays with green leaves"></div>
  <div class="night-band"></div>
  <svg class="footer-shape" width="1200" height="90" viewBox="0 0 1200 90">
    <polygon fill="#5ab4da" points="0,0 98,0 131,34 131,90 0,90"/>
    <polygon fill="#5ab4da" points="1069,34 1102,0 1200,0 1200,90 1069,90"/>
    <rect x="131" y="34" width="938" height="56" fill="#5ab4da"/>
  </svg>

  <svg class="header-shape" width="1200" height="97" viewBox="0 0 1200 97">
    <path fill="#ffffff" d="M38,0 L1162,0 L1085,86 Q1075,96 1060,96 L140,96 Q125,96 115,86 Z"/>
  </svg>
  <div class="top-line"></div>

  <div class="brand">TILDEN'S<br>BISCUIT BARN</div>

  <div class="contact phone">
    <svg width="13" height="14" viewBox="0 0 13 14"><path fill="#d10a0a" d="M2,1 L5,1 L6,4 L4,5.5 Q5.5,8.5 8.5,10 L10,8 L13,9 L13,12 Q12,14 9,13 Q2,10 0,3 Q0,1 2,1Z"/></svg>
    123-456-7890
  </div>
  <div class="contact email">
    <svg width="17" height="12" viewBox="0 0 17 12"><rect width="17" height="12" fill="#d10a0a"/><path d="M0,0 L8.5,7 L17,0" stroke="#fff" stroke-width="1.5" fill="none"/></svg>
    info@tildensbarn.net
  </div>
  <div class="book-button">BOOK A TABLE</div>
  <div class="header-rule"></div>

  <nav class="main-nav">
    <a class="active" href="#" style="width:68px">HOME</a>
    <a href="#" style="width:131px">ABOUT US</a>
    <a href="#" style="width:140px">OUR MENU</a>
    <a href="#" style="width:125px">GALLERY</a>
    <a href="#" style="width:150px">CONTACT US</a>
  </nav>

  <div class="caption-bar">
    <p class="caption-text">Lorem ipsum dolor sit amet, consectetur adipiscing elit</p>
    <div class="slider-dots"><span></span><span class="current"></span><span></span><span></span></div>
  </div>

  <section class="feature-panel">
    <svg class="welcome-shape" width="380" height="166" viewBox="0 0 380 166">
      <path fill="#ebe7d7" d="M0,0 L340,0 Q395,83 350,166 L0,166 Z"/>
    </svg>
    <p class="welcome-eyebrow">WELCOME TO</p>
    <h1 class="welcome-title">TILDEN'S BISCUIT BARN</h1>
    <p class="welcome-body">Lorem ipsum dolor sit ametconstuer adipiscing elit, sed diam nonummy nibh euismod tncidunt utm laoreet doore magna aliquam erat.</p>

    <div class="feature" style="left:393px">
      <svg width="86" height="86" viewBox="0 0 86 86">
        <defs><linearGradient id="g1" x1="0" y1="0" x2="0" y2="1"><stop offset="0" stop-color="#9ccc4f"/><stop offset="1" stop-color="#5d8f23"/></linearGradient></defs>
        <circle cx="43" cy="43" r="42" fill="url(#g1)"/>
        <rect x="27" y="22" width="32" height="42" rx="2" fill="none" stroke="#fff" stroke-width="3"/>
        <rect x="27" y="22" width="32" height="6" fill="#fff"/>
        <g stroke="#fff" stroke-width="2.5"><line x1="33" y1="35" x2="36" y2="35"/><line x1="39" y1="35" x2="53" y2="35"/><line x1="33" y1="42" x2="36" y2="42"/><line x1="39" y1="42" x2="53" y2="42"/><line x1="33" y1="49" x2="36" y2="49"/><line x1="39" y1="49" x2="53" y2="49"/><line x1="33" y1="56" x2="36" y2="56"/><line x1="39" y1="56" x2="53" y2="56"/></g>
      </svg>
      <p class="feature-label">OUR MENU</p>
    </div>
    <div class="feature-divider" style="left:573px"></div>
    <div class="feature" style="left:568px">
      <svg width="86" height="86" viewBox="0 0 86 86">
        <circle cx="43" cy="43" r="42" fill="url(#g1)"/>
        <rect x="24" y="27" width="28" height="34" rx="3" fill="none" stroke="#fff" stroke-width="3"/>
        <rect x="32" y="22" width="12" height="8" rx="2" fill="#fff"/>
        <rect x="38" y="38" width="24" height="28" rx="3" fill="#76a934" stroke="#fff" stroke-width="3"/>
        <polygon fill="#fff" points="50,44 52.5,49 58,49.5 54,53 55,58.5 50,56 45,58.5 46,53 42,49.5 47.5,49"/>
      </svg>
      <p class="feature-label">OUR SPECIAL</p>
    </div>
    <div class="feature-divider" style="left:738px"></div>
    <div class="feature" style="left:748px">
      <svg width="86" height="86" viewBox="0 0 86 86">
        <circle cx="43" cy="43" r="42" fill="url(#g1)"/>
        <path d="M43,68 Q25,48 25,36 A18,18 0 0 1 61,36 Q61,48 43,68Z" fill="none" stroke="#fff" stroke-width="3.5"/>
        <circle cx="43" cy="36" r="11" fill="#fff"/>
        <polygon fill="#76a934" points="43,29 45,33.5 50,34 46,37 47.5,42 43,39.5 38.5,42 40,37 36,34 41,33.5"/>
      </svg>
      <p class="feature-label">OUR LOCATION</p>
    </div>
  </section>

  <p class="copyright">© 2014 TILDENSBARN. All Rights Reserved.</p>
  <svg class="newsletter-icon" width="30" height="32" viewBox="0 0 30 32">
    <path fill="#ffffff" d="M15,0 L30,11 L30,32 L0,32 L0,11 Z"/>
    <path d="M0,12 L15,24 L30,12" fill="none" stroke="#5ab4da" stroke-width="1.5"/>
    <circle cx="15" cy="14" r="5" fill="none" stroke="#5ab4da" stroke-width="1.5"/>
  </svg>
  <div class="newsletter-input">Enter your email here</div>
  <div class="newsletter-go">GO</div>
  <div class="social-links"><span></span><span></span><span></span><span></span></div>
</div>
</body>
</html>
```